30 Nights of Lanterns Flyer Leading up to Easter

We want to push a campaign in March called 30 Nights of Lanterns. Its to get hope to you and bring hope through you. It will be daily emails and text messages of encouragement and challenges that will either encourage you or help you encourage someone else. I want to create a graphic that invites people to be a part of this 21 day challenge. This will be sponsored by our church. Ultimately, I will create an event on Facebook, Instagram and Tik Tok asking people to sign up to be a part of this 30 Nights of Lanterns campaign.

I need a graphic with the words:
30 Nights of Lanterns
To Get Hope to You and Bring Hope Through You
Beginning March 9th, leading up to Resurrection Weekend (Easter)
Brightwater Church (Logo) Included

Our church colors are red and blue. You will be able to pull those colors from the logo we upload. I will also upload some pics you can use but you don't have to use them. If there is better stock photos you have that would get the point across, please feel free. I would love this in 16x9 (1920x1080 px). I do have the AI or EPS fil for the logo if needed.
Updates

Another designer asked me to extend the deadline so they can submit. Will be choosing a design today. Marcus Fenwell

Target Market(s)

Thos who are hopeless and those who want to spread hope to others.

Industry/Entity Type

Church

Requirements
Must have
• These are in the description
Nice to have
• You don't have to use the pictures I sent. Stock photos are just fine. Would like a simple design as it is an invitation for people to join us in 30 Nights of Lanterns.

```html
<!DOCTYPE html>
<html lang="en">
<head>
<meta charset="utf-8">
<title>30 Nights of Lanterns</title>
<link rel="stylesheet" href="https://fonts.googleapis.com/css2?family=Jost:wght@400;500&family=Nunito:wght@900&family=Great+Vibes&display=swap">
<style>
  :root {
    --navy: #020266;
    --red: #e50307;
    --paper: #ffffff;
    --backdrop: #f2f2f2;
  }
  * { margin: 0; padding: 0; box-sizing: border-box; }
  html, body {
    width: 1200px; height: 1200px; overflow: hidden;
    background: var(--backdrop);
  }
  .flyer {
    position: absolute;
    left: 104px; top: 321px;
    width: 992px; height: 558px;
    background: var(--paper);
    overflow: hidden;
    font-family: "Jost", sans-serif;
    color: var(--navy);
  }
  .numeral {
    position: absolute;
    font-family: "Jost", sans-serif;
    font-weight: 500;
    font-size: 330px;
    line-height: 1;
    color: var(--navy);
  }
  .numeral--three { left: -14px; top: -40px; }
  .numeral--zero { left: 158px; top: 150px; }
  .script-word {
    position: absolute;
    left: 12px; top: 330px;
    font-family: "Great Vibes", cursive;
    font-size: 124px;
    line-height: 1;
    color: var(--red);
    transform: rotate(-6deg);
  }
  .bar { position: absolute; background: var(--red); }
  .bar--short-post { left: 266px; top: 41px; width: 19px; height: 130px; }
  .bar--tall-post { left: 299px; top: 0; width: 19px; height: 171px; }
  .bar--long-rule { left: 469px; top: 189px; width: 483px; height: 20px; }
  .bar--short-rule { left: 469px; top: 222px; width: 130px; height: 20px; }
  .vertical-title {
    position: absolute;
    left: 350px; top: 74px;
    writing-mode: vertical-rl;
    font-family: "Jost", sans-serif;
    font-weight: 500;
    font-size: 92px;
    line-height: 1;
    letter-spacing: -1px;
    color: var(--navy);
    white-space: nowrap;
  }
  .church-name {
    position: absolute;
    right: 40px; top: 78px;
    display: flex; align-items: center; gap: 10px;
    font-family: "Jost", sans-serif;
    font-weight: 500;
    font-size: 30px;
    color: var(--navy);
    white-space: nowrap;
  }
  .church-name__mark { width: 16px; height: 16px; background: var(--red); }
  .tagline {
    position: absolute;
    left: 500px; top: 264px; width: 430px;
    text-align: center;
    line-height: 1.3;
  }
  .tagline__line { font-size: 40px; font-weight: 400; }
  .tagline strong { font-family: "Nunito", sans-serif; font-weight: 900; }
  .tagline__line--accent {
    font-family: "Nunito", sans-serif; font-weight: 900;
    font-size: 52px; color: var(--red); line-height: 1.2;
  }
  .details {
    position: absolute;
    left: 520px; top: 454px; width: 440px;
    display: flex; align-items: center;
  }
  .details__start { width: 210px; text-align: center; }
  .details__divider { width: 1.5px; height: 78px; background: var(--red); }
  .details__end { width: 230px; text-align: center; }
  .details__label { font-size: 23px; line-height: 1.2; }
  .details__date {
    font-family: "Nunito", sans-serif; font-weight: 900;
    font-size: 29px; line-height: 1.2;
  }
  .details__event {
    font-family: "Nunito", sans-serif; font-weight: 900;
    font-size: 23px; line-height: 1.25;
  }
  .details__note { font-family: "Jost", sans-serif; font-weight: 400; color: var(--red); }
</style>
</head>
<body>
  <main class="flyer">
    <span class="numeral numeral--three">3</span>
    <span class="numeral numeral--zero">0</span>
    <span class="bar bar--short-post"></span>
    <span class="bar bar--tall-post"></span>
    <span class="script-word">nights</span>
    <span class="vertical-title">of Lanterns</span>

    <div class="church-name"><span class="church-name__mark"></span>Brightwater Church</div>

    <span class="bar bar--long-rule"></span>
    <span class="bar bar--short-rule"></span>

    <h1 class="tagline">
      <span class="tagline__line">To Get Hope to You</span><br>
      <span class="tagline__line">and <strong>Bring Hope</strong></span><br>
      <span class="tagline__line--accent">Through You</span>
    </h1>

    <section class="details">
      <div class="details__start">
        <p class="details__label">Beginning</p>
        <p class="details__date">March 9th</p>
      </div>
      <span class="details__divider"></span>
      <div class="details__end">
        <p class="details__label">Leading up to</p>
        <p class="details__event">Resurrection<br>Weekend <span class="details__note">(Easter)</span></p>
      </div>
    </section>
  </main>
</body>
</html>
```